Childrens Development/Fun Centre needs a Kid-Centric website

We need a website devoted to what we love, children, this site should be similar to other children development centre website which offer similar services and developments (best example - m a r r o w k i n . c o . u k)

We need to reflect our values of being fun and friendly whilst also imparting important skills and knowledge onto children. The website should have a button at the top for login (we are using the same MIS system as the example website listed above - so the login and members pages will be hosted by a third party site).

The site should incorporate a like us on facebook button, a instagram feed (please only use alpine phototile plugin for the instagram, for the twitter you can just use the standard code from twitter no need for a plugin)

We need to have mailpoet on the site too with a form to join our mailing list.

Initially we want to see some nice designs which are similar in feel and vibe of the logo which is enclosed, in a format the same as the example listed above.

thanks

Reason: Hi, Apologies for the delay and the miscommunication, we need this website actually CODED, the design can be directly based on the design of the website mentioned in the brief. please only submit or send me a message if your proposal was for CODING! thanks

```html
<!DOCTYPE html>
<html lang="en">
<head>
<meta charset="utf-8">
<title>PlayNest – Children's Development &amp; Fun Centre</title>
<link rel="stylesheet" href="https://fonts.googleapis.com/css2?family=Questrial&family=Shadows+Into+Light+Two&display=swap">
<style>
  :root {
    --green: #0aa14e;
    --green-light: #3cc66a;
    --wood-light: #f2bd82;
    --wood-mid: #e8a767;
    --wood-dark: #c98646;
    --brown: #8c5a1e;
    --brown-edge: #6e4414;
    --ink: #111111;
    --white: #ffffff;
    --purple-deep: #2a1050;
    --purple-mid: #3d1a63;
    --purple-warm: #6b3a55;
    --link: #6fa8ff;
    --logo-blue: #3b3f9f;
    --social: #ffffff;
    --font-body: "Questrial", Arial, sans-serif;
    --font-hand: "Shadows Into Light Two", "Comic Sans MS", cursive;
  }
  * { box-sizing: border-box; margin: 0; padding: 0; }
  html, body { width: 1200px; height: 900px; overflow: hidden; background: var(--white); }
  body { font-family: var(--font-body); color: var(--ink); }

  .page { position: relative; width: 1200px; height: 900px; overflow: hidden; }

  /* Header */
  .hero-art {
    position: absolute; left: 0; top: 0; width: 1200px; height: 236px;
    background:
      radial-gradient(ellipse 420px 180px at 1000px 230px, #5e8f5a 0%, #6c9d66 45%, rgba(108,157,102,0) 75%),
      radial-gradient(ellipse 300px 160px at 150px 90px, #fff6dc 0%, rgba(255,246,220,0) 80%),
      linear-gradient(100deg, #fbe6b8 0%, #fdf1d4 35%, #f9e2b4 60%, #f3d9a6 100%);
  }
  .brand {
    position: absolute; left: 52px; top: 82px;
    display: flex; align-items: center; gap: 14px;
    font-family: var(--font-body); font-size: 62px; line-height: 1;
    color: var(--logo-blue);
  }
  .brand-dot { width: 26px; height: 26px; border-radius: 50%; background: var(--green); }

  .top-tab { position: absolute; left: 718px; top: 0; width: 482px; height: 66px; }
  .top-tab svg { position: absolute; inset: 0; }
  .login {
    position: absolute; left: 773px; top: 15px;
    display: flex; align-items: center; gap: 12px;
    font-family: var(--font-hand); font-size: 24px; color: var(--white); text-decoration: none;
  }
  .login-icon { width: 36px; height: 36px; }
  .tab-divider { position: absolute; left: 899px; top: 15px; width: 1px; height: 35px; background: rgba(255,255,255,0.5); }
  .social { position: absolute; top: 14px; list-style: none; display: flex; gap: 21px; left: 933px; }
  .social li { width: 37px; height: 37px; border-radius: 50%; background: var(--social); opacity: 0.9; }

  /* Navigation */
  .main-nav {
    position: absolute; left: 0; top: 235px; width: 1200px; height: 50px;
    background: linear-gradient(180deg, var(--wood-mid) 0%, var(--wood-light) 30%, var(--wood-mid) 60%, var(--wood-light) 100%);
    box-shadow: 0 3px 4px rgba(0,0,0,0.12);
  }
  .main-nav ul { list-style: none; }
  .main-nav a {
    position: absolute; top: 6px; height: 36px; line-height: 36px;
    font-family: var(--font-hand); font-size: 24px; color: var(--ink); text-decoration: none;
    transform: translateX(-50%); white-space: nowrap;
  }
  .main-nav a.is-active {
    left: 175px; width: 110px; text-align: center; color: var(--white);
    background: var(--brown); border: 2px solid var(--brown-edge); border-radius: 5px;
  }

  /* Intro */
  .intro p {
    position: absolute; top: 297px; width: 380px;
    font-size: 18px; line-height: 24px; color: var(--ink); white-space: nowrap;
  }
  .intro .col-a { left: 50px; }
  .intro .col-b { left: 451px; }

  /* Newsletter */
  .newsletter {
    position: absolute; left: 0; top: 481px; width: 1200px; height: 120px;
    background: linear-gradient(180deg, var(--wood-light) 0%, var(--wood-mid) 25%, var(--wood-light) 50%, var(--wood-dark) 70%, var(--wood-light) 100%);
    box-shadow: 0 4px 6px rgba(0,0,0,0.35);
    z-index: 2;
  }
  .newsletter-icon { position: absolute; left: 103px; top: 38px; width: 66px; height: 46px; }
  .newsletter-title {
    position: absolute; left: 184px; top: 41px; white-space: nowrap;
    font-family: var(--font-hand); font-size: 28px; line-height: 36px; font-weight: 400; color: var(--white);
    letter-spacing: -0.5px; word-spacing: -3px;
    text-shadow: 1px 2px 3px rgba(0,0,0,0.45);
  }
  .newsletter-field {
    position: absolute; left: 531px; top: 34px; width: 420px; height: 53px;
    background: var(--white); border: 0; border-radius: 10px 0 0 10px;
  }
  .newsletter-submit {
    position: absolute; left: 929px; top: 33px; width: 168px; height: 54px;
    background: var(--brown); border: 0; border-radius: 10px;
    font-family: var(--font-hand); font-size: 32px; color: var(--white);
  }

  /* Footer */
  .footer-art {
    position: absolute; left: 0; top: 600px; width: 1200px; height: 300px;
    background:
      radial-gradient(circle 90px at 280px 70px, rgba(200,140,60,0.45), rgba(200,140,60,0)),
      radial-gradient(circle 110px at 930px 60px, rgba(180,80,60,0.4), rgba(180,80,60,0)),
      radial-gradient(circle 80px at 560px 170px, rgba(150,90,110,0.35), rgba(150,90,110,0)),
      linear-gradient(180deg, var(--purple-warm) 0%, var(--purple-mid) 40%, var(--purple-deep) 100%);
  }
  .footer-col { position: absolute; top: 637px; width: 200px; color: var(--white); }
  .footer-col h2 {
    font-weight: 400; font-size: 23px; line-height: 26px; padding-bottom: 4px;
    background-image: radial-gradient(circle, var(--white) 1.4px, transparent 1.6px);
    background-size: 6px 4px; background-repeat: repeat-x; background-position: 0 100%;
    width: 182px; height: 33px;
  }
  .footer-col ul { list-style: none; margin-top: 9px; }
  .footer-col li {
    position: relative; padding-left: 19px; margin-bottom: 9px; height: 45px;
    font-size: 10.5px; line-height: 15px; white-space: nowrap;
  }
  .footer-col li::before {
    content: ""; position: absolute; left: 3px; top: 3px; width: 8px; height: 8px;
    border-radius: 50%; background: var(--white);
  }
  .footer-col li a { color: var(--link); text-decoration: none; display: block; }
  .col-latest { left: 50px; }
  .col-archive { left: 357px; }
  .col-tweets { left: 661px; }
  .col-comments { left: 968px; }
  .copyright { position: absolute; left: 50px; top: 853px; font-size: 13px; color: var(--white); }
</style>
</head>
<body>
<div class="page">

  <header>
    <div class="hero-art" role="img" aria-label="Soft sunny illustrated landscape with bokeh light, a distant mountain and green treetops"></div>
    <div class="brand"><span>PlayNest</span><span class="brand-dot"></span></div>

    <div class="top-tab">
      <svg width="482" height="66" viewBox="0 0 482 66" aria-hidden="true">
        <path d="M0 0 H482 V38 Q482 64 455 64 H30 Q22 64 19 56 Z" fill="var(--green)"/>
      </svg>
    </div>
    <a class="login" href="#">Login
      <svg class="login-icon" viewBox="0 0 36 36" aria-hidden="true">
        <circle cx="18" cy="18" r="17" fill="var(--green-light)" stroke="#fff" stroke-width="2"/>
        <circle cx="18" cy="18" r="11" fill="#fff"/>
        <circle cx="18" cy="15" r="4" fill="var(--green-light)"/>
        <path d="M11 25 Q18 17 25 25 Z" fill="var(--green-light)"/>
      </svg>
    </a>
    <span class="tab-divider"></span>
    <ul class="social" aria-label="Social links">
      <li></li><li></li><li></li><li></li>
    </ul>
  </header>

  <nav class="main-nav">
    <ul>
      <li><a class="is-active" href="#">Home</a></li>
      <li><a href="#" style="left:451px">About Us</a></li>
      <li><a href="#" style="left:727px">Gallery</a></li>
      <li><a href="#" style="left:1003px">Contact us</a></li>
    </ul>
  </nav>

  <main class="intro">
    <p class="col-a">Lollipop candy canes I love topping I love.<br>Gummi bears lolly pops danish.<br>Liquorice sweet roll chocolate cake<br>macaroon candy dessert marshmallow<br>lemon drops toffee roll.</p>
    <p class="col-b">Croissant pudding powder tart powder<br>marshmallow. Powder brownie cookie<br>cotton candy candy canes.</p>
  </main>

  <section class="newsletter">
    <svg class="newsletter-icon" viewBox="0 0 66 46" aria-hidden="true">
      <rect x="1" y="1" width="64" height="44" fill="#fff" stroke="#6b4a2a" stroke-width="2"/>
      <path d="M1 1 L33 26 L65 1" fill="none" stroke="#6b4a2a" stroke-width="2"/>
      <path d="M1 45 L26 21 M65 45 L40 21" fill="none" stroke="#6b4a2a" stroke-width="2"/>
    </svg>
    <h2 class="newsletter-title">Sign up for our newsletter</h2>
    <input class="newsletter-field" type="email" aria-label="Email address">
    <button class="newsletter-submit" type="button">submit</button>
  </section>

  <footer>
    <div class="footer-art" role="img" aria-label="Deep purple background with soft glowing bokeh lights"></div>

    <section class="footer-col col-latest">
      <h2>Latest post</h2>
      <ul>
        <li>Jujubes chocolate bar I love<br>cookie. Tart gummies danish<br>cotton candy powder.</li>
        <li>Tiramisu sugar plum dessert<br>danish sweet roll jujubes I love<br>cheesecake carrot cake.</li>
        <li>Halvah tart candy fruitcake<br>danish. Bonbon apple cake I love<br>biscuit croissant chocolate.</li>
      </ul>
    </section>

    <section class="footer-col col-archive">
      <h2>Archives</h2>
      <ul>
        <li>[ June 01 ] Tart gummies danish<br>cotton candy powder. Sweet roll<br>marshmallow</li>
        <li>[ May 29 ] Tiramisu sugar plum<br>dessert danish sweet roll<br>jujubes I love carrot cake.</li>
        <li>[ May 27 ] Halvah candy<br>fruitcake danish. i love biscuit<br>croissant chocolate.</li>
      </ul>
    </section>

    <section class="footer-col col-tweets">
      <h2>Recent tweets</h2>
      <ul>
        <li>[ June 01 ] Tart gummies danish<br>cotton candy powder. Sweet roll<a href="#">tnyl.ink/4d5sad8</a></li>
        <li>[ May 29 ] Tiramisu sugar plum<br>dessert danish sweet roll<a href="#">tnyl.ink/785sda78</a></li>
        <li>[ May 27 ] Halvah candy<br>fruitcake danish. i love biscuit<a href="#">tnyl.ink/76sdsad8</a></li>
      </ul>
    </section>

    <section class="footer-col col-comments">
      <h2>Comments</h2>
      <ul>
        <li>[ @sam22 ] Tart gummies danish<br>cotton chocolate cake icing<br>topping...</li>
        <li>[ @lucy ] Icing brownie I love<br>bonbon topping wafer cake<br>muffin halvah...</li>
        <li>[ @tobin ] Wafer lolly pops<br>I love oat cake soufflé donut<br>marshmallow gummies...</li>
      </ul>
    </section>

    <p class="copyright">© 2014 PlayNest. All Rights Reserved</p>
  </footer>

</div>
</body>
</html>
```